Bold and modern Raw Manuka Honey label needed

We are needing a new label for one of our honey brands.
Raw Manuka honey has a lot of health benefits and we need a label to look appealing to health minded people but still looking like a jar of honey.
Manuka honey is a very high valued product that we export all over the world so we are looking for a clean and easy to read label as a lot of our customers are foreign and struggle with reading complex labels.
Be creative.... we have a logo and i will add it soon.
I was thinking of adding a silhouette of a bear to go with the Tumble Honey name but I'm very open to anything..
Target Market(s)
Health and medical retail shops.
Industry/Entity Type
Health And Wellness
Requirements
Must have
- Brand name is "velvo"
- Attached is our other label that we are looking at changing as well.
- Company details...
- Tumble Honey NZ Limited
- 4/18 Pellow Street
- Central Auckland
- PO Box 41-852
- Auckland
- tumblehoneynz@quillmarrow.com
- www.tumblehoneynz-quillmarrow.com
Nice to have
- Easy to read.
Should not have
- Hard to read fonts

```html
<!DOCTYPE html>
<html lang="en">
<head>
<meta charset="utf-8">
<title>Manuka Honay – Velvo Label</title>
<link href="https://fonts.googleapis.com/css2?family=Arimo:wght@400;700&display=swap" rel="stylesheet">
<style>
  :root{
    --canvas:#eeeeee;
    --label-bg:#f7f3f1;
    --panel:#ffffff;
    --pink:#f0396c;
    --brown:#6b3f14;
    --brown-dark:#4a2c10;
    --gold:#c9952b;
    --dark-band:#2b2a1c;
    --hex-inner:#2f2e22;
    --green:#3f7a18;
    --cream:#efe2b8;
    --ink:#222;
    --blossom:#f6d3dc;
  }
  *{box-sizing:border-box;margin:0;padding:0}
  html,body{width:1200px;height:1000px;overflow:hidden}
  body{background:var(--canvas);font-family:"Arimo",Arial,sans-serif;color:var(--ink);position:relative}

  .label{position:absolute;left:114px;top:335px;width:972px;height:330px;background:var(--label-bg);border:1px solid #d8d8d8}
  .label__strip{position:absolute;left:0;top:0;width:100%;height:8px;background:var(--pink)}

  .panel{position:absolute;top:8px;height:320px;background:var(--panel)}
  .panel--left{left:0;width:315px;border-top-right-radius:34px}
  .panel--right{left:655px;width:317px;border-top-left-radius:34px}

  .blossom{position:absolute;width:30px;height:30px;border-radius:50%;background:radial-gradient(circle,#e7a3b4 0 18%,var(--blossom) 20% 60%,transparent 62%)}

  /* left panel */
  .intro{position:absolute;left:38px;top:30px;width:248px;font-size:11.5px;line-height:1.15;color:var(--brown-dark);text-align:justify}
  .mgo-title{position:absolute;left:38px;top:102px;width:232px;text-align:center;font-size:11px;font-weight:700;color:var(--brown-dark)}
  .mgo-table{position:absolute;left:38px;top:117px;width:232px;border-collapse:collapse;font-size:11px;color:var(--brown-dark)}
  .mgo-table th{background:var(--brown);color:#fff;font-weight:400;height:16px;font-size:11px}
  .mgo-table td{height:16.5px;text-align:center}
  .mgo-table td:first-child{text-align:left;padding-left:12px}
  .grade-arrow{display:block;margin:0 auto}
  .company{position:absolute;left:38px;top:233px;width:236px;font-size:11px;color:var(--brown-dark);line-height:15px}
  .company b{font-size:12px}
  .company .row{display:flex;justify-content:space-between}
  .brand-mark--small{position:absolute;left:232px;top:278px;font-size:12px;font-weight:700;color:var(--brown)}

  /* centre panel */
  .front{position:absolute;left:315px;top:8px;width:340px;height:320px}
  .front__head{position:absolute;left:0;top:6px;width:340px;height:53px;background:var(--pink);text-align:center;color:#fff}
  .front__title{font-size:30px;font-weight:700;letter-spacing:.5px;line-height:34px;padding-top:5px}
  .front__sub{font-size:11px;font-weight:700;letter-spacing:2.6px;color:var(--brown-dark);line-height:12px}
  .front__rule{position:absolute;left:0;top:59px;width:340px;height:5px;background:var(--brown)}
  .front__hex{position:absolute;left:102px;top:71px}
  .front__brand{position:absolute;left:203px;top:76px;display:flex;align-items:center;gap:6px;font-size:17px;font-weight:700;color:var(--brown)}
  .front__brand i{width:18px;height:18px;border-radius:50%;background:var(--gold)}
  .front__fern{position:absolute;left:8px;top:199px;width:55px;height:28px;border-radius:4px;background:linear-gradient(135deg,#d9a83c,#b9832a)}
  .front__nz{position:absolute;left:8px;top:229px;font-size:8px;font-weight:700;color:var(--gold)}
  .front__cert{position:absolute;left:106px;top:223px;font-size:12px;font-weight:700;color:var(--green)}
  .front__weight{position:absolute;left:258px;top:196px;font-size:31px;font-weight:700;color:var(--gold)}
  .front__band{position:absolute;left:0;top:249px;width:340px;height:71px;background:var(--dark-band);text-align:center}
  .front__band i{display:block;width:14px;height:14px;border-radius:50%;background:var(--gold);margin:13px auto 0}
  .front__company{display:block;margin-top:14px;font-size:14px;color:var(--cream)}

  /* right panel */
  .nutri-title{position:absolute;left:66px;top:44px;font-size:20px;font-weight:700;color:var(--brown)}
  .nutri{position:absolute;left:66px;top:70px;width:191px;border-collapse:collapse;font-size:9px;color:var(--ink);line-height:1.1}
  .nutri td{border:1px solid var(--brown);padding:2px 3px;vertical-align:top}
  .nutri td.q{text-align:center;width:36px}
  .nutri .big{font-size:10.5px}
  .site{position:absolute;left:66px;top:262px;width:191px;text-align:center;font-size:11px;color:var(--brown-dark)}
</style>
</head>
<body>
<div class="label">
  <div class="label__strip"></div>

  <section class="panel panel--left">
    <span class="blossom" role="img" aria-label="manuka blossom" style="left:270px;top:10px"></span>
    <span class="blossom" role="img" aria-label="manuka blossom" style="left:8px;top:85px"></span>
    <span class="blossom" role="img" aria-label="manuka blossom" style="left:190px;top:262px"></span>
    <p class="intro">Velvo brings you 35 years of quality honay, Our honay are 100% pure natural and nothing added. Honay the way it should bee. Best stored at room temperature and away from direct sunlight.</p>
    <h3 class="mgo-title">DIETARY MGO CONTENT</h3>
    <table class="mgo-table">
      <thead><tr><th>MGO</th><th>NPA</th><th>GRADE</th></tr></thead>
      <tbody>
        <tr><td>MGO30+</td><td>2+</td><td>General</td></tr>
        <tr><td>MGO100+</td><td>5+</td><td rowspan="3"><svg class="grade-arrow" width="10" height="46" viewBox="0 0 10 46"><line x1="5" y1="0" x2="5" y2="38" stroke="#222" stroke-width="1.5"/><path d="M1 36 L5 46 L9 36Z" fill="#222"/></svg></td></tr>
        <tr><td>MGO250+</td><td>10+</td></tr>
        <tr><td>MGO500+</td><td>15+</td></tr>
        <tr><td>MGO800+</td><td>20+</td><td>Premium</td></tr>
      </tbody>
    </table>
    <div class="company">
      <div class="row"><b>Tumble Honey NZ Limited</b><span><b>PO Box</b> 41-852</span></div>
      <div>4/18 Pellow Street, Auckland Central, New Zealand</div>
      <div><b>Export ID</b> HIVE7 <b>THB</b>2291</div>
      <div><b>Best before</b> January 2019</div>
    </div>
    <span class="brand-mark--small">VELVO</span>
  </section>

  <section class="front">
    <span class="blossom" role="img" aria-label="manuka blossom" style="left:28px;top:98px"></span>
    <span class="blossom" role="img" aria-label="manuka blossom" style="left:222px;top:195px"></span>
    <header class="front__head">
      <h1 class="front__title">MANUKA HONAY</h1>
      <p class="front__sub">PREMIUM NEW ZEALAND HONAY</p>
    </header>
    <div class="front__rule"></div>
    <svg class="front__hex" width="132" height="150" viewBox="0 0 132 150">
      <polygon points="66,2 130,38 130,112 66,148 2,112 2,38" fill="var(--gold)"/>
      <polygon points="66,12 121,43 121,107 66,138 11,107 11,43" fill="var(--hex-inner)"/>
      <circle cx="66" cy="75" r="42" fill="#f3dde3" role="img" aria-label="manuka flower illustration"/>
    </svg>
    <div class="front__brand">VELVO<i></i></div>
    <div class="front__fern" role="img" aria-label="silver fern emblem"></div>
    <span class="front__nz">NEW ZEALAND</span>
    <span class="front__cert">CERTIFIED MGO 800+</span>
    <span class="front__weight">500g</span>
    <div class="front__band"><i></i><span class="front__company">Tumble Honey NZ Limited</span></div>
  </section>

  <section class="panel panel--right">
    <span class="blossom" role="img" aria-label="manuka blossom" style="left:2px;top:33px"></span>
    <span class="blossom" role="img" aria-label="manuka blossom" style="left:235px;top:15px"></span>
    <span class="blossom" role="img" aria-label="manuka blossom" style="left:280px;top:178px"></span>
    <span class="blossom" role="img" aria-label="manuka blossom" style="left:128px;top:275px"></span>
    <h2 class="nutri-title">MANUKA HONAY</h2>
    <table class="nutri">
      <tr><td><span class="big">NUTRITIONAL<br>INFORMATION</span><br>Servings per package: 50<br>Serving size: 10g</td><td class="q"><br>Qty<br>per<br>Serve</td><td class="q"><br>Qty<br>per<br>100g</td></tr>
      <tr><td>Energy</td><td class="q">132kJ</td><td class="q">1320kJ</td></tr>
      <tr><td>Protein</td><td class="q">&lt;0.1g</td><td class="q">0.4g</td></tr>
      <tr><td>Total Fat<br>&nbsp;- Saturated</td><td class="q">0g<br>0g</td><td class="q">0g<br>0g</td></tr>
      <tr><td>Carbohydrates<br>&nbsp;- Sugars</td><td class="q">8.0g<br>7.8g</td><td class="q">80g<br>78g</td></tr>
      <tr><td>Sodium</td><td class="q">1.2mg</td><td class="q">12mg</td></tr>
      <tr><td colspan="3">INGREDIENTS: 100% Pure New Zealand Honey, Pollen. Certified MGO 800+</td></tr>
    </table>
    <p class="site">www.tumblehoneynz-quillmarrow.com</p>
  </section>
</div>
</body>
</html>
```